3 Business Card designs for a company with multiple services

We are a company that has 3 main services:

1) Security - CCTV & Alarm Sepcialists
2) Broadcast - Broadcast Sales and Technical Services
3) Distribution - Quality Products, Quality Service

The broadcast service is for Video Broadcast.

I will include our logos for each service.

I would like to also create a business card design for 7QK in general (see main logo).

Each card will be two-sided. On the front I would think it would include Logo, Name, Posistion and Mobile (and possibly email). And possibly our main number (which may be something like 1800 639 415)

On the back it MUST include a "lined" section to be able to write short quotes / prices.

Then include more details like Phone: 1800 639 415 Fax: 1800 639 412 Postal: PO Box 731, Tallowen, QLD Australia 4290 Website: www.7qk.com.au

We would like a fresh, inovative card design with that "wow check this out" feel about it.

Look forward to seeing what you can do! :)

Corey

Industry/Entity Type

Business

Requirements
Must have
• Quote section on the back!
Editable files.

```html
<!DOCTYPE html>
<html lang="en">
<head>
<meta charset="utf-8">
<title>7QK Business Cards</title>
<link rel="stylesheet" href="https://fonts.googleapis.com/css2?family=Michroma&display=swap">
<style>
  :root {
    --page: #ffffff;
    --band-dark: #1c1c1c;
    --band-mid: #3a3a3a;
    --band-light: #5a5a5a;
    --body-dark: #8f8f8f;
    --body-light: #e8e8e8;
    --ink: #3b3b3b;
    --ink-soft: #555555;
    --paper-text: #ffffff;
    --back-text: #cfcfcf;
    --broadcast: #f0a418;
    --distribution: #1e4aa8;
    --security: #c9c9c9;
    --general: #8a8a8a;
    --rule: #cfcfcf;
    --quote-line-light: rgba(60, 60, 60, 0.45);
    --quote-line-dark: rgba(200, 200, 200, 0.35);
  }
  * { margin: 0; padding: 0; box-sizing: border-box; }
  html, body {
    width: 1200px; height: 514px; overflow: hidden;
    background: var(--page);
    font-family: "Michroma", "Arial", sans-serif;
  }
  .sheet { position: relative; width: 1200px; height: 514px; }
  .card { position: absolute; width: 388px; height: 238px; overflow: hidden; }
  .row-top { top: 8px; }
  .row-bottom { top: 276px; }
  .col-1 { left: 5px; }
  .col-2 { left: 410px; }
  .col-3 { left: 808px; }

  /* Front */
  .front .header {
    position: absolute; left: 0; top: 0; width: 100%; height: 100px;
    background: linear-gradient(90deg, var(--band-dark) 0%, var(--band-dark) 55%, var(--band-mid) 80%, var(--band-light) 100%);
  }
  .front .brand {
    position: absolute; left: 0; top: 0; height: 100px; width: 340px;
    display: flex; align-items: center; gap: 14px; padding-left: 14px;
  }
  .brand .mark { width: 46px; height: 46px; flex: none; }
  .mark.broadcast { background: var(--broadcast); }
  .mark.distribution { background: var(--distribution); }
  .mark.security { background: var(--security); }
  .mark.general { background: var(--general); }
  .brand .brand-name {
    color: var(--paper-text); font-size: 15px; letter-spacing: 2px; white-space: nowrap;
  }
  .front .body {
    position: absolute; left: 0; top: 100px; width: 100%; height: 138px;
    background: linear-gradient(90deg, var(--body-dark) 0%, #b9b9b9 45%, var(--body-light) 100%);
  }
  .person { position: absolute; left: 190px; top: 36px; color: var(--ink); }
  .person .name { font-size: 13px; letter-spacing: 3px; }
  .person .role { font-size: 8px; letter-spacing: 1.5px; margin-top: 6px; color: var(--ink-soft); }
  .contact-line {
    position: absolute; left: 16px; right: 12px; bottom: 16px;
    display: flex; justify-content: space-between;
    font-size: 8px; letter-spacing: 1px; color: var(--ink); white-space: nowrap;
  }

  /* Back */
  .back .top-band {
    position: absolute; left: 0; top: 0; width: 100%; height: 60px;
    border-radius: 0 16px 0 0;
    background: linear-gradient(180deg, #5a5a5a 0%, #2e2e2e 50%, #1e1e1e 100%);
    color: var(--back-text); font-size: 9px; letter-spacing: 2px;
    display: flex; align-items: center; padding-left: 78px;
  }
  .back .rule {
    position: absolute; left: 0; right: 0; top: 78px; height: 2px; background: var(--rule);
  }
  .back .body { position: absolute; left: 0; top: 88px; width: 100%; height: 150px; }
  .back.light .body { background: linear-gradient(90deg, #d7d7d7 0%, #9e9e9e 45%, #e3e3e3 100%); }
  .back.dark .body { background: linear-gradient(90deg, #2a2a2a 0%, #101010 50%, #2c2c2c 100%); }

  .quote-lines {
    position: absolute; left: 16px; right: 14px; top: 14px;
    list-style: none;
  }
  .quote-lines li { height: 22px; border-bottom: 1px solid var(--quote-line-light); }
  .back.dark .quote-lines li { border-bottom-color: var(--quote-line-dark); }

  .back .details {
    position: absolute; left: 16px; right: 14px; bottom: 14px;
    font-size: 8.5px; letter-spacing: 1px; line-height: 18px; white-space: nowrap;
  }
  .back.light .details { color: var(--ink); }
  .back.dark .details { color: var(--back-text); }
  .details .split { display: flex; justify-content: space-between; }
</style>
</head>
<body>
<main class="sheet">

  <section class="card front row-top col-1">
    <div class="header">
      <div class="brand"><span class="mark broadcast"></span><span class="brand-name">7QK BROADCAST</span></div>
    </div>
    <div class="body">
      <div class="person"><p class="name">Neil Hartley</p><p class="role">Guitar</p></div>
      <div class="contact-line"><span>Mobile 1800 639 415</span><span>Email:office@7qk.com.au</span></div>
    </div>
  </section>

  <section class="card front row-top col-2">
    <div class="header">
      <div class="brand"><span class="mark general"></span><span class="brand-name">7QK GROUP</span></div>
    </div>
    <div class="body">
      <div class="person"><p class="name">Neil Hartley</p><p class="role">Guitar</p></div>
      <div class="contact-line"><span>Mobile 1800 639 415</span><span>Email:office@7qk.com.au</span></div>
    </div>
  </section>

  <section class="card back light row-top col-3">
    <div class="top-band">Website: www.7qk.com.au</div>
    <div class="rule"></div>
    <div class="body">
      <ul class="quote-lines" aria-label="Quote lines"><li></li><li></li><li></li></ul>
      <div class="details">
        <div class="split"><span>Phone: 1800 639 415</span><span>Fax: 1800 639 412</span></div>
        <div>Postal: PO Box 731, Tallowen, QLD Australia 4290</div>
      </div>
    </div>
  </section>

  <section class="card front row-bottom col-1">
    <div class="header">
      <div class="brand"><span class="mark distribution"></span><span class="brand-name">7QK DISTRIBUTION</span></div>
    </div>
    <div class="body">
      <div class="person"><p class="name">Neil Hartley</p><p class="role">Guitar</p></div>
      <div class="contact-line"><span>Mobile 1800 639 415</span><span>Email:office@7qk.com.au</span></div>
    </div>
  </section>

  <section class="card front row-bottom col-2">
    <div class="header">
      <div class="brand"><span class="mark security"></span><span class="brand-name">7QK SECURITY</span></div>
    </div>
    <div class="body">
      <div class="person"><p class="name">Neil Hartley</p><p class="role">Guitar</p></div>
      <div class="contact-line"><span>Mobile 1800 639 415</span><span>Email:office@7qk.com.au</span></div>
    </div>
  </section>

  <section class="card back dark row-bottom col-3">
    <div class="top-band">Website: www.7qk.com.au</div>
    <div class="rule"></div>
    <div class="body">
      <ul class="quote-lines" aria-label="Quote lines"><li></li><li></li><li></li></ul>
      <div class="details">
        <div class="split"><span>Phone: 1800 639 415</span><span>Fax: 1800 639 412</span></div>
        <div>Postal: PO Box 731, Tallowen, QLD Australia 4290</div>
      </div>
    </div>
  </section>

</main>
</body>
</html>
```